One Page / Executive Summary for Bright Harbor Executive Search

We would need an executive summary for our firm Bright Harbor Executive Search - like a small one pager which we can via PDF to our clients.
It should include like the file 23030 all Infos - Only Track Record needs to be complemented
But it should be designed much nicer than it is now - also open for new design situations but it should fit our website concept www.brightharbor.io
It should also include a graph of the recruiting process - maybe draw a new one.?
We would need a very elegant, modern, slim design, it should look very female - it should not have a green color block on the top but be more sleek bright and with our bird
Target Market(s)
CEO, HR executives
Industry/Entity Type
HR Consultantcy
Font styles to use
Other font styles liked:
- Calibri, cost or robotic condensed
Requirements
Must have
- sleek slim modern elegant design, ideally a white side with a frame or with our bird
Nice to have
- project progress on our website, female modern, elegant design, not too overloaded, possibility to complement our text
Should not have
- no petrol color block as on our website or as in our proposal, prefer a white background with our photo as a log,

```html
<!DOCTYPE html>
<html lang="en">
<head>
<meta charset="utf-8">
<title>Bright Harbor Executive Search – Executive Summary</title>
<link href="https://fonts.googleapis.com/css2?family=Roboto+Condensed:wght@300;400;700&family=Roboto:wght@300;400&display=swap" rel="stylesheet">
<style>
:root{
  --teal:#0b4f63;
  --sky:#8ab8c8;
  --ring:#bcdbe5;
  --ink:#6d6d6d;
  --dark:#1c1c1c;
  --paper:#ffffff;
  --backdrop:#e4e6e8;
  --panel:#f3f8fa;
}
*{box-sizing:border-box;margin:0;padding:0}
html,body{width:1200px;height:1200px;overflow:hidden;background:var(--backdrop)}
body{font-family:"Roboto",sans-serif;color:var(--ink)}
.page{position:absolute;left:176px;top:0;width:848px;height:1200px;background:var(--paper);overflow:hidden}
.abs{position:absolute}

/* header */
.brand{left:40px;top:130px;display:flex;align-items:center;gap:14px}
.brand-dot{width:48px;height:48px;border-radius:50%;background:var(--ring)}
.brand-name{font-family:"Roboto Condensed",sans-serif;font-weight:300;font-size:31px;letter-spacing:5px;color:var(--teal)}
.headline{left:30px;top:214px;font-family:"Roboto Condensed",sans-serif;font-weight:400}
.headline .soft{display:block;font-size:30px;line-height:26px;color:var(--sky);text-transform:uppercase}
.headline .strong{display:block;font-size:46px;line-height:46px;margin-top:4px;color:var(--teal);font-weight:700}

.portrait-ring{left:402px;top:-118px;width:516px;height:516px;border-radius:50%;background:var(--ring)}
.portrait{left:420px;top:-100px;width:480px;height:480px;border-radius:50%;background:radial-gradient(circle at 55% 40%,#3a3a3a,#161616 70%)}
.person{font-family:"Roboto Condensed",sans-serif;color:#fff;font-size:15px;line-height:17px;white-space:nowrap}
.person b{font-weight:700;display:block}
.person span{font-weight:300;font-size:14px}

/* headings */
.h2{font-family:"Roboto Condensed",sans-serif;font-weight:700;font-size:20px;line-height:25px;color:var(--teal)}
.h2 em{font-style:normal;color:var(--sky)}
.h2::after{content:"";display:block;width:26px;height:2px;background:var(--teal);margin-top:4px}

/* ticks */
.ticks{list-style:none;font-size:13.5px;line-height:18.6px;color:var(--ink)}
.ticks li{position:relative;padding-left:17px}
.ticks li::before{content:"";position:absolute;left:0;top:5px;width:10px;height:10px;border:1.3px solid var(--teal);border-radius:50%}
.ticks li::after{content:"";position:absolute;left:3.5px;top:6.5px;width:3px;height:5px;border-right:1.4px solid var(--teal);border-bottom:1.4px solid var(--teal);transform:rotate(40deg)}
.ticks.spaced{line-height:17px}
.ticks.spaced li{margin-bottom:6px;text-align:justify}
.ticks.numbers{line-height:17px}
.ticks.numbers li{margin-bottom:4px}

.intro{font-size:13.5px;line-height:17px;text-align:justify;width:352px}

/* industries */
.industries{left:430px;top:444px;display:flex;width:380px;justify-content:space-between}
.industry{width:92px;text-align:center;font-family:"Roboto Condensed",sans-serif;font-size:15px;line-height:14px;color:var(--dark)}
.industry .icon{width:52px;height:52px;margin:0 auto 14px;border-radius:50%;background:linear-gradient(160deg,var(--teal),var(--sky))}

/* process */
.process{left:440px;top:869px;width:364px;height:167px;background:var(--panel);border-radius:12px}

/* footer */
.loc-label{left:0;width:848px;top:1050px;text-align:center;font-family:"Roboto Condensed",sans-serif;font-size:23px;line-height:26px;color:#444}
.loc-band{left:20px;width:808px;top:1080px;height:38px;background:linear-gradient(90deg,rgba(11,79,99,0) 0%,var(--teal) 18%,var(--teal) 82%,rgba(11,79,99,0) 100%);display:flex;justify-content:center;gap:48px;align-items:center;font-family:"Roboto Condensed",sans-serif;font-size:23px;color:#fff}
.contact{font-family:"Roboto Condensed",sans-serif;font-size:19px;line-height:22px;color:var(--teal);display:flex;align-items:center;gap:7px;white-space:nowrap}
.social{display:flex;gap:10px}
.social i{display:block;width:31px;height:31px;border-radius:50%;background:var(--teal)}
</style>
</head>
<body>
<main class="page">

  <div class="abs portrait-ring"></div>
  <div class="abs portrait" role="img" aria-label="Photograph of the two managing directors against a dark background"></div>
  <div class="abs person" style="left:520px;top:294px"><b>Clara Vossberg</b><span>Managing Director</span></div>
  <div class="abs person" style="left:645px;top:294px"><b>Dr. Helena Marquardt</b><span>Managing Director</span></div>

  <div class="abs brand"><span class="brand-dot"></span><span class="brand-name">BRIGHT HARBOR</span></div>

  <h1 class="abs headline">
    <span class="soft">So, they don’t</span>
    <span class="soft">wear ties in the</span>
    <span class="soft">boardroom anymore</span>
    <span class="strong">WE NEVER DID...</span>
  </h1>

  <!-- left column -->
  <h2 class="abs h2" style="left:38px;top:378px">What <em>we do:</em></h2>
  <p class="abs intro" style="left:40px;top:413px">While we consider ourselves a boutique Executive Search Firm our span across Europe and covers multiple industries:</p>
  <ul class="abs ticks" style="left:40px;top:468px">
    <li>General Healthcare</li><li>Hospitals &amp; Medical Practices</li><li>Medical Technology</li><li>Medical Association</li>
  </ul>
  <ul class="abs ticks" style="left:266px;top:468px">
    <li>Education</li><li>Venture Capital</li><li>Private Equity</li><li>Consumer</li>
  </ul>

  <h2 class="abs h2" style="left:38px;top:563px;width:280px">Typically we recruit for <em>these types of roles</em></h2>
  <ul class="abs ticks" style="left:40px;top:626px">
    <li>CEO</li><li>COO</li><li>CMO</li>
  </ul>
  <ul class="abs ticks" style="left:126px;top:626px">
    <li>Venture Capital Partner</li><li>Operations Partner PE</li><li>President</li>
  </ul>

  <h2 class="abs h2" style="left:38px;top:708px">How <em>we work:</em></h2>
  <ul class="abs ticks spaced" style="left:40px;top:743px;width:352px">
    <li>Longstanding experience with a passion for placing C-Level Executives in the Healthcare, Consumer and Venture Capital industry</li>
    <li>We work with you personally and act as an ambassador for our clients in the market</li>
    <li>Engaging on eye-level discussion beyond just placement and HR topics</li>
    <li>Structured and lean digital search processes, creative approaches, high transparency, comprehensive candidate evaluation</li>
    <li>Extensive referencing of candidates as part of the search process; psychometrics on demand</li>
    <li>Onboarding support to ensure a good start for the candidate</li>
  </ul>

  <!-- right column -->
  <h2 class="abs h2" style="left:439px;top:405px">Industries</h2>
  <div class="abs industries">
    <div class="industry"><div class="icon" role="img" aria-label="Healthcare icon"></div>Healthcare</div>
    <div class="industry"><div class="icon" role="img" aria-label="Private capital icon"></div>Private<br>Capital</div>
    <div class="industry"><div class="icon" role="img" aria-label="Consumer icon"></div>Consumer</div>
    <div class="industry"><div class="icon" role="img" aria-label="Education icon"></div>Education &amp;<br>Administration</div>
  </div>

  <h2 class="abs h2" style="left:442px;top:555px">By the <em>numbers:</em></h2>
  <ul class="abs ticks numbers" style="left:443px;top:593px;width:360px">
    <li>95% retention rate over the course of two years</li>
    <li>30 placements made with Bright Harbor</li>
    <li>In total 20 years of experience in the Executive search sector</li>
  </ul>

  <h2 class="abs h2" style="left:443px;top:688px">Track <em>Record</em></h2>
  <ul class="abs ticks spaced" style="left:443px;top:724px;width:364px">
    <li>In 2022 we merged with Marlene Osterkamp -beratung im Gesundheitswesen GmbH &amp; Co. Marlene Osterkamp -beratung im Gesundheitswesen</li>
    <li>Since November 2022 we have also been working with Lindqvist-Rahe GbR.</li>
  </ul>

  <h2 class="abs h2" style="left:442px;top:839px">Recruiting <em>process:</em></h2>
  <div class="abs process">
    <svg width="364" height="167" viewBox="0 0 528 242" font-family="Roboto Condensed, sans-serif" fill="#0b4f63" text-anchor="middle">
      <g font-weight="700" font-size="10">
        <text x="110" y="30">Phase 1</text><text x="110" y="43">Research - LONGLIST</text>
        <text x="282" y="30">Phase 2</text><text x="282" y="43">Fokus &amp; Interviews - SHORTLIST</text>
        <text x="449" y="30">Phase 3</text><text x="449" y="43">Abschluss</text>
      </g>
      <line x1="28" y1="65" x2="514" y2="65" stroke="#1c1c1c" stroke-width="2.5"/>
      <g stroke="#0b4f63" stroke-dasharray="2 2">
        <line x1="55" y1="65" x2="55" y2="82"/><line x1="237" y1="65" x2="237" y2="82"/><line x1="447" y1="65" x2="447" y2="82"/>
        <line x1="143" y1="65" x2="143" y2="146"/><line x1="362" y1="65" x2="362" y2="146"/>
      </g>
      <g fill="#8ab8c8" stroke="#fff" stroke-width="1.5">
        <circle cx="55" cy="65" r="4"/><circle cx="143" cy="65" r="4"/><circle cx="237" cy="65" r="4"/><circle cx="362" cy="65" r="4"/><circle cx="447" cy="65" r="4"/>
        <circle cx="55" cy="94" r="13"/><circle cx="237" cy="94" r="13"/><circle cx="447" cy="94" r="13"/>
      </g>
      <circle cx="143" cy="160" r="14"/><circle cx="362" cy="160" r="14"/>
      <g font-weight="700" font-size="10">
        <text x="55" y="125">Kickoff</text><text x="240" y="125">Interviews</text><text x="449" y="125">Kandidatenauswahl</text>
        <text x="143" y="195">Research</text><text x="362" y="196">Referenzen</text>
      </g>
      <g font-size="7" fill="#444">
        <text x="55" y="141">Abstimmung Profil,</text><text x="55" y="153">Positionsbeschreibung und</text><text x="55" y="165">Zielfirmenliste</text>
        <text x="240" y="141">Präsentation der priorisierten</text><text x="240" y="153">Profile, Klienteninterviews</text>
        <text x="449" y="141">Vertragsverhandlung und</text><text x="449" y="153">Onboarding, Feedback</text><text x="449" y="165">Gespräch</text>
        <text x="143" y="209">Aktiver und passive Research,</text><text x="143" y="221">Ansprache pot. Kandidat*innen</text>
        <text x="362" y="210">Ggf. Assessment, Einholen von</text><text x="362" y="222">Referenzen</text>
      </g>
    </svg>
  </div>

  <!-- footer -->
  <div class="abs loc-label">LOCATIONS</div>
  <div class="abs loc-band"><span>HAMBURG</span><span>WIEN</span><span>MÜNCHEN</span><span>DÜSSELDORF</span></div>

  <div class="abs contact" style="left:40px;top:1132px">
    <svg width="14" height="12" viewBox="0 0 14 12"><rect x="1" y="1" width="12" height="10" rx="1" fill="none" stroke="#0b4f63" stroke-width="1.5"/><path d="M1 2 L7 7 L13 2" fill="none" stroke="#0b4f63" stroke-width="1.5"/></svg>
    applications@brightharbor.io
  </div>
  <div class="abs contact" style="left:40px;top:1157px">
    <svg width="13" height="13" viewBox="0 0 14 14"><circle cx="7" cy="7" r="6" fill="none" stroke="#0b4f63" stroke-width="1.3"/><ellipse cx="7" cy="7" rx="2.6" ry="6" fill="none" stroke="#0b4f63" stroke-width="1.1"/><line x1="1" y1="7" x2="13" y2="7" stroke="#0b4f63" stroke-width="1.1"/></svg>
    www.brightharbor.io
  </div>
  <div class="abs contact" style="left:352px;top:1132px">
    <svg width="13" height="13" viewBox="0 0 14 14"><path d="M3 1 L5.5 1 L6.5 4.5 L4.8 5.8 C5.6 7.6 6.6 8.6 8.2 9.3 L9.5 7.6 L13 8.6 L13 11 C13 12 12 13 11 13 C5.5 12.5 1.5 8.5 1 3 C1 2 2 1 3 1 Z" fill="#0b4f63"/></svg>
    +49 151 20 648 519
  </div>
  <div class="abs social" style="left:685px;top:1129px" aria-label="Social media links">
    <i></i><i></i><i></i>
  </div>

</main>
</body>
</html>
```